Company Profile
Korvane Cargo Sdn Bhd is a well-established and experienced freight forwarder in Kuala Lumpur, Malaysia. We specialize in air and sea forwarding, Custom Brokerage and regulatory compliance services, inland transportation, overseas freighting and warehousing and distribution management. With our dedicated qualified and experienced professionals, we are fully committed to serving our clients.

Our Mission
Based on the motto “Quick, Reliable and Polite”, Korvane Cargo is dedicated to upholding the following three points corporate philosophy:1. Adhering to the principle that “the customer always comes first”.2. Contributing to the development of the local community.3. Making it our duty to be responsible and sincere.

Our Edge
• One-Stop Logistics Solutions
• Extensive Network Throughout Malaysia
• Highly Qualified and Experienced Pool of Professionals
• Comprehensive IT Solutions
• Innovative and Customer-focused Solutions
• Flexible and Consistent in Managing Exceptions
• Total Supply Chain Visibility

Target Market : We sell the logistics services to all the industry in Malaysia. (One Stop Logistics Solutions)

Business Card Detail : I would like to see the logo on the front with the general info.

Must Haves :
1) Name, Title, Office, Cell, Fax, Email, Address, Website
2) Must have complete company name show as : Korvane Cargo Sdn Bhd
3) Must have company registration no, show as : 8571620-W

Nice to Haves : Modern Design Business Card

Target Market(s)

We sell the logistics services to all the industry in Malaysia. (One Stop Logistics Solutions)

Contact Information for Business Card

I would like to see the logo on the front with the general info.

Colors

Designer to choose colors to be used in the design.

Requirements
Must have
• 1) Name, Title, Office, Cell, Fax, Email, Address, Website
• 2) Must have complete company name show as : Korvane Cargo Sdn Bhd
• 3) Must have company registration no, show as : 8571620-W
Nice to have
• Modern Design Business Card
Should not have
• Nil

```html
<!DOCTYPE html>
<html lang="en">
<head>
<meta charset="utf-8">
<title>Korvane Cargo – Business Card</title>
<link rel="stylesheet" href="https://fonts.googleapis.com/css2?family=Open+Sans:ital,wght@0,400;0,600;0,700;1,400&display=swap">
<style>
  :root {
    --stage: #3a3532;
    --card: #1d1f22;
    --ink: #f2f2f2;
    --silver: #b9bcc0;
    --blue: #1f64ae;
    --blue-light: #2ea3dc;
    --rule: #8a8d91;
  }
  * { box-sizing: border-box; margin: 0; padding: 0; }
  html, body { width: 1200px; height: 864px; overflow: hidden; }
  body {
    background: var(--stage);
    font-family: "Open Sans", sans-serif;
    color: var(--ink);
    position: relative;
  }
  .card {
    position: absolute;
    left: 250px;
    width: 700px;
    height: 400px;
    background: var(--card);
    border-radius: 4px;
    box-shadow: 0 8px 24px rgba(0,0,0,.45);
  }
  .card--back { top: 21px; }
  .card--front { top: 443px; }

  /* back side */
  .brand-row {
    position: absolute;
    top: 62px; left: 0; right: 0;
    display: flex; align-items: center; justify-content: center; gap: 22px;
  }
  .brand-dot {
    width: 64px; height: 64px; border-radius: 50%;
    border: 4px solid var(--silver);
  }
  .brand-name {
    font-size: 40px; font-weight: 600; letter-spacing: 3px;
    color: var(--silver); text-transform: uppercase;
  }
  .edge-list {
    position: absolute; top: 180px; left: 40px; right: 40px;
    text-align: center; font-size: 17px; line-height: 28px;
  }
  .tagline {
    position: absolute; bottom: 40px; left: 0; right: 0;
    text-align: center; font-size: 18px; font-style: italic; color: var(--blue);
  }

  /* front side */
  .reg-no {
    position: absolute; top: 22px; left: 30px; font-size: 13px;
  }
  .mark {
    position: absolute; top: 90px; left: 46px; width: 250px;
    display: flex; flex-direction: column; align-items: center; gap: 16px;
  }
  .mark-circle {
    width: 170px; height: 170px; border-radius: 50%;
    border: 7px solid var(--blue);
  }
  .mark-name {
    font-size: 24px; font-weight: 700; color: var(--blue); letter-spacing: 1px;
  }
  .divider { position: absolute; left: 318px; top: 70px; }
  .contact {
    position: absolute; left: 352px; top: 66px; right: 24px;
    font-size: 15px; line-height: 21px;
  }
  .person-name { font-size: 24px; font-weight: 700; color: var(--blue); line-height: 28px; }
  .person-title { font-size: 17px; color: var(--blue-light); margin-bottom: 8px; }
  .address { margin-bottom: 8px; }
  .contact-line { display: flex; align-items: center; gap: 9px; }
  .contact-line svg { width: 14px; height: 14px; flex: none; fill: var(--ink); }
</style>
</head>
<body>

<section class="card card--back">
  <div class="brand-row">
    <div class="brand-dot"></div>
    <div class="brand-name">Korvane Cargo</div>
  </div>
  <p class="edge-list">
    One-Stop Logistics Solutions • Extensive Network Throughout Malaysia<br>
    Highly Qualified &amp; Experienced Pool of Professionals<br>
    Comprehensive IT Solutions • Innovative &amp; Customer-focused Solutions<br>
    • Flexible &amp; Consistent in Managing Exceptions • Total Supply Chain Visibility
  </p>
  <p class="tagline">One Stop Logistics Specialist</p>
</section>

<section class="card card--front">
  <p class="reg-no">Reg No: 8571620-W</p>
  <div class="mark">
    <div class="mark-circle"></div>
    <div class="mark-name">Korvane Cargo</div>
  </div>
  <svg class="divider" width="14" height="280" viewBox="0 0 14 280">
    <line x1="13" y1="0" x2="1" y2="280" stroke="var(--rule)" stroke-width="1.2"/>
  </svg>
  <div class="contact">
    <p class="person-name">DANIEL TAN</p>
    <p class="person-title">Managing Director</p>
    <p class="address">
      Korvane Cargo Sdn Bhd<br>
      No.8B, 2nd Floor,<br>
      Jalan Seri Kembang 4/KS2,<br>
      Taman Mutiara, 41150 Klang,<br>
      Selangor Darul Ehsan, Malaysia.
    </p>
    <p class="contact-line">
      <svg viewBox="0 0 16 16"><path d="M3 1h3l1.5 4-2 1.3a9 9 0 0 0 4.2 4.2L11 8.5l4 1.5v3c0 1-1 2-2 2C6.5 15 1 9.5 1 3c0-1 1-2 2-2z"/></svg>
      (+603) 3342 7180 / 7181
    </p>
    <p class="contact-line">
      <svg viewBox="0 0 16 16"><path d="M4 0h8a1 1 0 0 1 1 1v14a1 1 0 0 1-1 1H4a1 1 0 0 1-1-1V1a1 1 0 0 1 1-1zm0 2v10h8V2zm4 11a1 1 0 1 0 0 2 1 1 0 0 0 0-2z"/></svg>
      (+6012) 574 2906
    </p>
    <p class="contact-line">
      <svg viewBox="0 0 16 16"><path d="M4 0h7v4H4zM1 5h14v7h-3v4H4v-4H1zm4 6v4h6v-4z"/></svg>
      (+603) 3342 7182
    </p>
    <p class="contact-line">
      <svg viewBox="0 0 16 16"><path d="M0 3h16v1L8 9 0 4zm0 3 8 5 8-5v7H0z"/></svg>
      daniel.tan@korvanecargo.com.my
    </p>
    <p class="contact-line">
      <svg viewBox="0 0 16 16"><circle cx="8" cy="8" r="7.5"/></svg>
      www.korvanecargo.com.my
    </p>
  </div>
</section>

</body>
</html>
```